Harborline Motors LLC

Car Dealer Customer Service
Address: 2741 Linden Avenue, Shelbyville, TN 37162
web: www.harborlinemotorstn.net
email: harborlinemotorstn@mailbox-example.net
Phone: (931) 555-0148
Phone: (629) 555-0173

```html
<!DOCTYPE html>
<html lang="en">
<head>
<meta charset="utf-8">
<title>Harborline Motors – Business Cards</title>
<link rel="stylesheet" href="https://fonts.googleapis.com/css2?family=Montserrat:wght@400;600;700;800&family=Questrial&display=swap">
<style>
  :root {
    --backdrop: #2a2e35;
    --mustard: #e9b447;
    --mustard-soft: #efc265;
    --teal: #1c8f8a;
    --ink: #2b2b2b;
    --grey: #6d6d6d;
    --paper: #ffffff;
    --violet: #7b3fb8;
  }
  * { box-sizing: border-box; margin: 0; padding: 0; }
  html, body { width: 1200px; height: 781px; overflow: hidden; }
  body {
    background: var(--backdrop);
    display: flex;
    align-items: center;
    justify-content: center;
    gap: 60px;
    font-family: "Montserrat", sans-serif;
  }
  .card {
    position: relative;
    width: 510px;
    height: 292px;
    border-radius: 3px;
    overflow: hidden;
    box-shadow: 0 10px 30px rgba(0,0,0,.35);
  }

  /* Front */
  .card-front { background: var(--mustard); }
  .front-pattern {
    position: absolute; inset: 0;
    background: radial-gradient(circle at 50% 50%, var(--mustard-soft), var(--mustard) 75%);
  }
  .front-brand {
    position: absolute; inset: 0;
    display: flex; flex-direction: column; align-items: center; justify-content: center;
    color: var(--paper);
  }
  .brand-row { display: flex; align-items: center; gap: 14px; }
  .brand-dot { width: 38px; height: 38px; border-radius: 50%; background: var(--teal); }
  .brand-name {
    font-weight: 800; font-size: 34px; letter-spacing: 1px; text-transform: uppercase;
  }
  .tagline {
    margin-top: 8px; font-weight: 600; font-size: 12px; letter-spacing: 2.5px; text-transform: uppercase;
  }

  /* Back */
  .card-back { background: var(--paper); }
  .tab {
    position: absolute; left: 0; top: 30px; width: 6px; height: 36px; background: var(--violet);
    border-radius: 0 3px 3px 0;
  }
  .person { position: absolute; left: 26px; top: 30px; }
  .person-name { font-size: 20px; color: var(--teal); letter-spacing: .5px; text-transform: uppercase; }
  .person-name strong { font-weight: 800; }
  .person-role { font-family: "Questrial", sans-serif; font-size: 12px; color: var(--grey); margin-top: 2px; }

  .back-brand {
    position: absolute; right: 30px; top: 120px;
    display: flex; align-items: center; gap: 10px;
  }
  .back-brand .brand-dot { width: 30px; height: 30px; background: var(--mustard); }
  .back-brand .brand-name { font-size: 20px; color: var(--teal); letter-spacing: .5px; }

  .contact { font-family: "Questrial", sans-serif; font-size: 9.5px; color: var(--ink); }
  .contact-list { position: absolute; left: 26px; top: 180px; list-style: none; }
  .contact-list li, .contact-phone { display: flex; align-items: center; gap: 7px; }
  .contact-list li + li { margin-top: 7px; }
  .contact-phone { position: absolute; right: 30px; bottom: 24px; }
  .icon { width: 10px; height: 10px; flex: none; }
</style>
</head>
<body>

<section class="card card-front">
  <div class="front-pattern" role="img" aria-label="Repeating pattern of the company emblem in soft mustard tones"></div>
  <div class="front-brand">
    <div class="brand-row">
      <span class="brand-dot"></span>
      <span class="brand-name">Harborline Motors</span>
    </div>
    <p class="tagline">Car Dealer Customer Service</p>
  </div>
</section>

<section class="card card-back">
  <span class="tab"></span>
  <div class="person">
    <p class="person-name">Person <strong>Name</strong></p>
    <p class="person-role">President</p>
  </div>

  <div class="back-brand">
    <span class="brand-dot"></span>
    <span class="brand-name">Harborline Motors</span>
  </div>

  <ul class="contact contact-list">
    <li>
      <svg class="icon" viewBox="0 0 10 10"><circle cx="5" cy="5" r="4.3" fill="none" stroke="#2b2b2b" stroke-width="1"/><path d="M.7 5h8.6M5 .7c-2 2.6-2 5.9 0 8.6M5 .7c2 2.6 2 5.9 0 8.6" fill="none" stroke="#2b2b2b" stroke-width=".8"/></svg>
      www.harborlinemotorstn.net
    </li>
    <li>
      <svg class="icon" viewBox="0 0 10 10"><rect x=".5" y="2" width="9" height="6.5" rx=".8" fill="#2b2b2b"/><path d="M1 2.6l4 3 4-3" fill="none" stroke="#fff" stroke-width=".8"/></svg>
      harborlinemotorstn@mailbox-example.net
    </li>
  </ul>

  <p class="contact contact-phone">
    <svg class="icon" viewBox="0 0 10 10"><path d="M2.2.8l1.6 2-1 1.1c.6 1.3 1.6 2.3 2.9 2.9l1.1-1 2 1.6-.9 1.6C5 8.8 1.2 5 .6 1.7z" fill="#2b2b2b"/></svg>
    + (931) 555-0148, (629) 555-0173
  </p>
</section>

</body>
</html>
```